Geometric 4 color design for operating room and recovery room floors

I am looking for two geometric designs (I have attached examples) for an operating room and a recovery room floor. The floor will be four colors: Dark Blue, Middle Blue, Light Blue, and White (as in the photos). The designs need, respectively, to fill in rectangles of the following proportions: OR is 25 feet vertical by 17 feet horizontal. Recovery room is a 17x17 foot square. From the photos, I want the recovery room to look exactly like the photo that I am attaching (but the perspective on the photos needs to be looking straight down, so I can give the plan to the people who are cutting the vinyl sheets). The Operating room will need to have the colors reversed from the photo I have uploaded - an 8x8 foot dark blue circle under the OR table and then going from dark blue to middle blue to light blue to white from the center to the walls (white at the walls). Thank you!!

```html
<!DOCTYPE html>
<html lang="en">
<head>
<meta charset="utf-8">
<title>Operating Room Floor Plan</title>
<link rel="stylesheet" href="https://fonts.googleapis.com/css2?family=Jost:wght@300;400&display=swap">
<style>
  :root {
    --page-bg: #ffffff;
    --floor-white: #fbfdfe;
    --outline-blue: #0b3aa8;
    --light-blue: #c4effe;
    --middle-blue: #6dcefe;
    --dark-blue: #00339e;
    --label-ink: #111111;
  }
  html, body {
    margin: 0;
    padding: 0;
    width: 1200px;
    height: 1000px;
    overflow: hidden;
    background: var(--page-bg);
  }
  .canvas {
    position: relative;
    width: 1200px;
    height: 1000px;
    background: var(--page-bg);
    overflow: hidden;
  }
  .floor-plan {
    position: absolute;
    left: 0;
    top: 0;
    width: 1200px;
    height: 1000px;
    shape-rendering: geometricPrecision;
  }
  .floor-plan .zone {
    shape-rendering: geometricPrecision;
  }
  .room-label {
    position: absolute;
    left: 0;
    width: 1200px;
    top: 919px;
    margin: 0;
    text-align: center;
    font-family: "Jost", "Futura", sans-serif;
    font-weight: 300;
    font-size: 23px;
    line-height: 34px;
    letter-spacing: 1px;
    color: var(--label-ink);
    white-space: nowrap;
  }
</style>
</head>
<body>
  <main class="canvas">
    <svg class="floor-plan" viewBox="0 0 1200 1000" xmlns="http://www.w3.org/2000/svg" aria-label="Operating room floor with concentric blue zones">
      <rect class="room-outline" x="150" y="195" width="902" height="613" fill="var(--floor-white)" stroke="var(--outline-blue)" stroke-width="2"/>
      <ellipse class="zone zone-light" cx="601" cy="501" rx="434" ry="281" fill="var(--light-blue)"/>
      <ellipse class="zone zone-middle" cx="601" cy="501" rx="306" ry="198" fill="var(--middle-blue)"/>
      <ellipse class="zone zone-table" cx="601" cy="501" rx="144" ry="144.5" fill="var(--dark-blue)"/>
    </svg>
    <p class="room-label">OPERATING ROOM</p>
  </main>
</body>
</html>
```